Harborline Works Buisness Cards

Provide a business card layout

Peter Landry
PO Box 915
Wrenfield MA 01234
peter@hworksllc-example.com

Industry/Entity Type

Business

Font styles to use
Serif

Colors
f04a50

```html
<!DOCTYPE html>
<html lang="en">
<head>
<meta charset="UTF-8">
<title>Harborline Works – Business Card</title>
<link href="https://fonts.googleapis.com/css2?family=Cinzel:wght@700&family=Lato:wght@400;700;900&display=swap" rel="stylesheet">
<style>
  :root {
    --backdrop: #5e5e5e;
    --card: #ffffff;
    --brand-red: #f04a50;
    --ink: #1a1a1a;
    --band-black: #0d0d0d;
    --gold: #e6a532;
    --white: #ffffff;
  }
  * { margin: 0; padding: 0; box-sizing: border-box; }
  html, body {
    width: 1200px;
    height: 900px;
    overflow: hidden;
    background: var(--backdrop);
  }
  .business-card {
    position: absolute;
    left: 100px;
    top: 165px;
    width: 1000px;
    height: 570px;
    background: var(--card);
    overflow: hidden;
    box-shadow: 0 10px 30px rgba(0,0,0,0.35);
  }
  .brand {
    position: absolute;
    top: 120px;
    left: 0;
    width: 100%;
    display: flex;
    align-items: center;
    justify-content: center;
    gap: 22px;
  }
  .brand-dot {
    width: 46px;
    height: 46px;
    border-radius: 50%;
    background: var(--gold);
  }
  .brand-name {
    font-family: "Cinzel", serif;
    font-weight: 700;
    font-size: 56px;
    color: var(--ink);
    letter-spacing: 1px;
  }
  .person-name {
    position: absolute;
    top: 248px;
    left: 0;
    width: 100%;
    text-align: center;
    font-family: "Lato", sans-serif;
    font-size: 60px;
    color: var(--brand-red);
    letter-spacing: 1px;
  }
  .person-name .first { font-weight: 400; }
  .person-name .last { font-weight: 900; }
  .contact-band {
    position: absolute;
    left: 440px;
    right: 0;
    bottom: 0;
    height: 135px;
    background: var(--band-black);
    display: flex;
    align-items: center;
    padding-left: 60px;
    gap: 14px;
  }
  .email-tab {
    position: absolute;
    left: 0;
    bottom: 0;
    width: 490px;
    height: 175px;
    background: var(--brand-red);
    border-top-right-radius: 36px;
    display: flex;
    align-items: flex-end;
    padding: 0 0 48px 36px;
    gap: 14px;
  }
  .contact-text {
    font-family: "Lato", sans-serif;
    font-size: 26px;
    color: var(--white);
    white-space: nowrap;
  }
  .email .contact-text { font-weight: 700; }
  .address .contact-text { font-weight: 400; }
  .icon { flex: none; }
</style>
</head>
<body>
  <main class="business-card">
    <div class="brand">
      <span class="brand-dot"></span>
      <span class="brand-name">Harborline Works</span>
    </div>

    <h1 class="person-name"><span class="first">PETER</span> <span class="last">LANDRY</span></h1>

    <div class="contact-band address">
      <svg class="icon" width="22" height="32" viewBox="0 0 22 32" aria-hidden="true">
        <path d="M11 0C4.9 0 0 4.9 0 11c0 8 11 21 11 21s11-13 11-21C22 4.9 17.1 0 11 0z" fill="var(--gold)"/>
        <circle cx="11" cy="11" r="4.5" fill="var(--band-black)"/>
      </svg>
      <span class="contact-text">PO Box 915, Wrenfield MA 01234</span>
    </div>

    <div class="email-tab email">
      <svg class="icon" width="30" height="22" viewBox="0 0 32 24" aria-hidden="true">
        <rect x="0" y="0" width="32" height="24" rx="2" fill="var(--white)"/>
        <path d="M1 2 L16 14 L31 2" fill="none" stroke="var(--brand-red)" stroke-width="2.5"/>
      </svg>
      <span class="contact-text">peter@hworksllc-example.com</span>
    </div>
  </main>
</body>
</html>
```